SunnyPawLand Webshop and Logo Design

We need a complete design for our new Webshop
We sell pet accessories for dogs, cats, guinea pigs and some other animals
The provided logo ist a first draft for our logo and not final. you can be creative.
Maybe you can bring in some "Happyness" :o)
The Website will be a PressKit/KartMill System with a "ShopCanvas" Theme. We can provide a test environment, but it must be transferable to the final website.
In the First step, we need a finalized logo, then the WebDesign.

We need the following items.

* Company Icon
* Favicon 512*512 (from company icon)
* Shipping Label Icon (300px*100px, transparent background)
* Label Icon (600px*150px, transparent background)
* WebShop Design/Child-Theme
* Businesscard

Target Market(s)

German retail for pet accessories

Industry/Entity Type

Pet

Logo Text

SunnyPawLand

Coding

Coded - Design and coding required

Number of Pages Required

3 page

Colors

Designer to choose colors to be used in the design.

Requirements
Must have
• Cat, Dog, and Guineapig must be present
• The design must communicate happy pets.

```html
<!DOCTYPE html>
<html lang="en">
<head>
<meta charset="utf-8">
<title>SunnyPawLand – Pet Accessories Webshop</title>
<link href="https://fonts.googleapis.com/css2?family=Poppins:ital,wght@0,400;0,500;0,600;1,400&family=Open+Sans:ital,wght@0,400;0,600;0,700;1,400&display=swap" rel="stylesheet">
<style>
:root{
  --green-dark:#2a9a3e;
  --green-btn:#3f8a2c;
  --green-card:#a9e2aa;
  --mint-bg:#dcefe1;
  --blue-head:#1b4e94;
  --navy:#23406e;
  --red:#d2312f;
  --ink:#333333;
  --muted:#666666;
  --paper:#f6f6f4;
  --beige:#ddd5c4;
  --footer:#2b251b;
  --sky:#5bb9e4;
  --white:#ffffff;
}
*{box-sizing:border-box;margin:0;padding:0}
html,body{width:1200px;height:2965px;overflow:hidden}
body{position:relative;background:var(--paper);font-family:"Open Sans",Arial,sans-serif;color:var(--ink)}
.abs{position:absolute}
.head-font{font-family:"Poppins",Arial,sans-serif}

/* header */
.header-bg{left:0;top:0;width:1200px;height:702px;background:var(--mint-bg)}
.header-notch{left:585px;top:700px;width:0;height:0;border-left:15px solid transparent;border-right:15px solid transparent;border-top:15px solid var(--mint-bg)}
.topbar{left:0;top:0;width:1200px;height:44px;background:var(--green-dark)}
.topbar-links{right:88px;top:0;height:44px;display:flex;gap:24px;align-items:center;color:var(--white);font-family:"Poppins",sans-serif;font-size:11px;letter-spacing:.3px}
.topbar-links .phone{font-size:14px;font-weight:500}
.topbar-links svg{vertical-align:-2px;margin-right:5px}
.brand{left:82px;top:100px;display:flex;align-items:center;gap:10px}
.brand-dot{width:40px;height:40px;border-radius:50%;background:var(--blue-head)}
.brand-name{font-family:"Poppins",sans-serif;font-weight:600;font-size:30px;color:var(--green-dark)}
.account-row{right:88px;top:66px;display:flex;gap:26px;align-items:center;font-family:"Poppins",sans-serif;font-size:11px;color:var(--ink)}
.account-row .welcome{color:var(--red)}
.cart-box{border:1px solid #bbb;background:var(--white);padding:6px 10px;font-size:11px}
.main-nav{right:88px;top:133px;display:flex;gap:30px;font-family:"Poppins",sans-serif;font-size:13px;font-weight:500;color:#222}

/* hero */
.hero{left:85px;top:192px;width:1028px;height:460px;border:7px solid var(--white);box-shadow:0 0 6px rgba(0,0,0,.2);background:linear-gradient(160deg,#e9e4dc 0%,#b99a7a 45%,#6c4a32 75%,#d9d3cb 100%)}
.hero-panel{left:310px;top:324px;width:528px;height:272px;background:rgba(40,40,40,.72);text-align:center;color:var(--white)}
.hero-title{font-family:"Poppins",sans-serif;font-weight:500;font-size:44px;letter-spacing:1px;margin-top:40px}
.hero-text{font-size:13px;line-height:20px;margin:14px 40px 0}
.btn{display:inline-block;background:var(--green-btn);color:var(--white);font-family:"Poppins",sans-serif;font-size:11px;font-weight:500;text-align:center;border-bottom:3px solid #2a6419;border-radius:2px}
.hero-btn{width:118px;height:44px;line-height:42px;margin-top:28px}

/* section titles */
.section-title{left:0;width:1200px;text-align:center;font-family:"Poppins",sans-serif;font-size:36px;color:var(--blue-head)}
.title-rule{left:500px;width:200px;height:2px;background:#cfcfcf}

/* categories */
.cat-card{top:850px;width:247px;height:297px;background:var(--green-card);border-radius:3px;box-shadow:0 2px 3px rgba(0,0,0,.2);text-align:center}
.cat-tab{position:absolute;left:98px;top:-8px;width:50px;height:12px;background:var(--white);border-radius:3px 3px 0 0}
.cat-icon{width:122px;height:122px;border-radius:50%;margin:42px auto 0;background:#e8f7e8;border:3px dashed var(--white)}
.cat-name{font-family:"Poppins",sans-serif;font-size:17px;margin-top:22px;color:#222}
.cat-desc{font-size:12px;color:#444;margin-top:2px}
.cat-btn{width:118px;height:38px;line-height:36px;margin-top:14px}

/* welcome */
.video{left:85px;top:1378px;width:421px;height:247px;border:7px solid #2a5da8;background:linear-gradient(120deg,#8c9aa8,#c98e7a 45%,#8d6e5d 75%,#5b6f87)}
.video-bar{left:92px;top:1592px;width:407px;height:26px;background:rgba(30,30,30,.8)}
.welcome-lead{left:536px;top:1372px;width:580px;font-size:17px;line-height:26px;color:#333}
.welcome-body{left:536px;top:1440px;width:580px;font-size:12px;line-height:20px;color:#555;text-align:justify}
.welcome-link{left:536px;top:1592px;font-size:15px;font-weight:700;color:var(--blue-head)}

/* featured */
.product{top:1858px;width:245px;height:287px;background:var(--white);border:1px solid #ddd;text-align:center}
.product-img{height:208px}
.product-name{font-family:"Poppins",sans-serif;font-size:15px;margin-top:12px;color:#222}
.product-price{font-family:"Poppins",sans-serif;font-weight:600;font-size:19px;color:#2d8f3a;margin-top:14px;border-top:1px solid #e4e4e4;padding-top:8px}
.quick{left:110px;width:140px;height:32px;background:var(--navy);color:var(--white);font-size:12px;line-height:32px;padding-left:14px;border-radius:2px}

/* testimonials */
.testi-bg{left:0;top:2200px;width:1200px;height:317px;background:var(--beige)}
.testi-title{top:2243px;font-size:28px}
.medal-string{left:160px;top:2193px}
.medal{left:100px;top:2278px;width:166px;height:166px;border-radius:50%;background:#9e9384;border:10px solid #cfc7b7;box-shadow:0 2px 4px rgba(0,0,0,.3)}
.medal-inner{width:126px;height:126px;border-radius:50%;margin:10px;background:linear-gradient(#ffffff,#e6e2da)}
.quote{left:270px;top:2310px;font-family:"Poppins",sans-serif;font-style:italic;font-size:24px;color:#222}
.quote-body{left:270px;top:2352px;width:850px;font-style:italic;font-size:12px;line-height:18px;color:#333}
.quote-name{left:270px;top:2424px;font-size:13px;color:var(--red)}
.dots{left:1022px;top:2458px;display:flex;gap:5px}
.dots span{width:13px;height:13px;border-radius:50%;background:#999}
.dots span:first-child{background:#444}

/* footer */
.footer{left:0;top:2517px;width:1200px;height:294px;background:linear-gradient(#3a3124,var(--footer))}
.foot-head{font-family:"Poppins",sans-serif;font-size:17px;color:var(--white);letter-spacing:.5px}
.foot-text{font-size:11.5px;line-height:19px;color:#ddd}
.foot-nav{display:grid;grid-template-columns:96px 100px;row-gap:11px;font-size:11.5px;color:#eee}
.post-thumb{left:677px;top:2634px;width:123px;height:86px;background:linear-gradient(135deg,#b05a86,#e79bbb);border:2px solid #555}
.post-date{font-style:italic;color:#6cb8e6;font-size:11.5px}

/* subscribe */
.subscribe{left:0;top:2811px;width:1200px;height:154px;background:var(--sky)}
.sub-title{left:85px;top:2840px;font-family:"Poppins",sans-serif;font-weight:500;font-size:26px;color:var(--white)}
.sub-text{left:85px;top:2878px;font-size:12.5px;color:var(--white)}
.sub-input{left:412px;top:2845px;width:372px;height:44px;border:2px solid var(--white);border-radius:22px;padding:0 18px;line-height:40px;font-size:12.5px;color:var(--white)}
.social{top:2846px;width:40px;height:40px;border-radius:50%;border:2px solid var(--white)}
.copy-rule{left:0;top:2916px;width:1200px;height:1px;background:rgba(255,255,255,.5)}
.copyright{left:0;top:2932px;width:1200px;text-align:center;font-size:11px;color:var(--white)}
</style>
</head>
<body>

<div class="abs header-bg"></div>
<div class="abs header-notch"></div>

<div class="abs topbar"></div>
<div class="abs topbar-links">
  <span><svg width="12" height="12" viewBox="0 0 12 12"><circle cx="6" cy="3.5" r="3" fill="#fff"/><path d="M0 12c0-4 3-5 6-5s6 1 6 5z" fill="#fff"/></svg>MY ACCOUNT</span>
  <span><svg width="12" height="11" viewBox="0 0 12 11"><path d="M6 10.5 1 5.5A3 3 0 0 1 6 1.5a3 3 0 0 1 5 4z" fill="none" stroke="#fff" stroke-width="1.4"/></svg>WISH LIST (0)</span>
  <span class="phone"><svg width="13" height="13" viewBox="0 0 13 13"><path d="M3 1l2 3-1.3 1.3a7 7 0 0 0 4 4L9 8l3 2-1.5 2.5C5.5 12 1 7.5.5 2.5z" fill="#fff"/></svg>555-010-2040</span>
</div>

<div class="abs brand">
  <div class="brand-dot"></div>
  <div class="brand-name">SunnyPawLand</div>
</div>

<div class="abs account-row">
  <span class="welcome">WELCOME</span>
  <span>LOGIN</span>
  <span>CREATE AN ACCOUNT</span>
  <span class="cart-box">0 item(s) - $0.00</span>
</div>

<nav class="abs main-nav">
  <span>HOME</span><span>ABOUT US</span><span>SHOP</span><span>BLOG</span><span>DELIVERY</span><span>FAQS</span><span>CONTACT US</span>
</nav>

<div class="abs hero" role="img" aria-label="Photo of a small dog holding a brown leather leash in its mouth"></div>
<div class="abs hero-panel">
  <div class="hero-title">DOG ACCESSORIES</div>
  <p class="hero-text">Lorem ipsum dolor sit amet, consectetuer adipiscing elit, sed diam nonummy nibh euismod tincidunt ut laoreet.</p>
  <span class="btn hero-btn">SHOP NOW</span>
</div>

<h2 class="abs section-title" style="top:750px">OUR PRODUCTS CATEGORY</h2>
<div class="abs title-rule" style="top:810px"></div>

<div class="abs cat-card" style="left:83px"><div class="cat-tab"></div><div class="cat-icon" role="img" aria-label="Cat icon"></div><div class="cat-name">CAT ACCESSORIES</div><div class="cat-desc">Lorem ipsum dolor sit consectetuer</div><span class="btn cat-btn">VIEW ALL</span></div>
<div class="abs cat-card" style="left:344px"><div class="cat-tab"></div><div class="cat-icon" role="img" aria-label="Dog icon"></div><div class="cat-name">DOGS</div><div class="cat-desc">Lorem ipsum dolor sit consectetuer</div><span class="btn cat-btn">VIEW ALL</span></div>
<div class="abs cat-card" style="left:603px"><div class="cat-tab"></div><div class="cat-icon" role="img" aria-label="Guinea pig icon"></div><div class="cat-name">GUINEA PIGS</div><div class="cat-desc">Lorem ipsum dolor sit consectetuer</div><span class="btn cat-btn">VIEW ALL</span></div>
<div class="abs cat-card" style="left:864px"><div class="cat-tab"></div><div class="cat-icon" role="img" aria-label="Rat icon"></div><div class="cat-name">RATS</div><div class="cat-desc">Lorem ipsum dolor sit consectetuer</div><span class="btn cat-btn">VIEW ALL</span></div>

<h2 class="abs section-title" style="top:1264px">WELCOME TO SUNNYPAWLAND</h2>
<div class="abs title-rule" style="top:1322px"></div>

<div class="abs video" role="img" aria-label="Video still of a smiling couple on a sofa holding a small white dog"></div>
<div class="abs video-bar"></div>
<p class="abs welcome-lead">Exerci tation ullamcorper suscipit lobortis nisl commodo conseuis autem vel eum iriure dolor in hendrerit in vulputate velit esse.</p>
<p class="abs welcome-body">Lorem ipsum dolor sit amet, consectetuer adipiscing elit, sed diam nonummy nibh euismod tincidunt ut laoreet dolore magna aliquam erat volutpat. Ut wisi enim ad minim venia quis nostrud exerci tation ullamcorper suscipit lobortis nisl ut aliquip ex ea commodo consequat. Duis autem vel eum iriure dolor in hendrerit in vulputate velit esse molestie consequa vel illum dolore eu feugiat nulla facilisis at vero eros et accumsan et iusto odio dim qui blandit praesent luptatum zzril delenit augue duis dolore te feugait nulla facilisi.</p>
<p class="abs welcome-link">Got questions? We've got answers.</p>

<h2 class="abs section-title" style="top:1750px">FEATURED PRODUCTS</h2>
<div class="abs title-rule" style="top:1808px"></div>

<div class="abs product" style="left:83px"><div class="product-img" role="img" aria-label="Dark photo of a dog accessory" style="background:linear-gradient(135deg,#3a2a22,#6a4a38)"></div><div class="product-name">Dog Accessory One</div><div class="product-price">$10.00</div></div>
<div class="abs quick" style="top:1907px">Add to cart</div>
<div class="abs quick" style="top:1955px">Add to Wishlist</div>
<div class="abs quick" style="top:2003px">Quick View</div>
<div class="abs product" style="left:344px"><div class="product-img" role="img" aria-label="Photo of kittens eating from a green bowl" style="background:linear-gradient(135deg,#e8e2da,#b9b3a8 60%,#c3d64a)"></div><div class="product-name">Cat Food One</div><div class="product-price">$10.00</div></div>
<div class="abs product" style="left:605px"><div class="product-img" role="img" aria-label="Photo of a bowl of dry pet food" style="background:linear-gradient(160deg,#a8693a,#e9e3d8 55%,#f2eee8)"></div><div class="product-name">Food One</div><div class="product-price">$10.00</div></div>
<div class="abs product" style="left:867px"><div class="product-img" role="img" aria-label="Photo of a white dog wearing pink sunglasses against blue sky" style="background:linear-gradient(135deg,#5bb6e8,#cfe9f6 55%,#e0d7c8)"></div><div class="product-name">Cat Food One</div><div class="product-price">$10.00</div></div>

<div class="abs testi-bg"></div>
<svg class="abs" style="left:0;top:2507px" width="1200" height="20" viewBox="0 0 1200 20" aria-hidden="true">
  <defs><pattern id="scallop" width="20" height="20" patternUnits="userSpaceOnUse"><circle cx="10" cy="10" r="10" fill="#2b251b"/></pattern></defs>
  <rect x="0" y="10" width="1200" height="10" fill="url(#scallop)"/>
</svg>
<h2 class="abs section-title testi-title">WHAT OUR CUSTOMERS SAY</h2>
<svg class="abs medal-string" width="50" height="100" viewBox="0 0 50 100" aria-hidden="true"><path d="M8 0 L23 90 M36 0 L23 90" stroke="#d8a82a" stroke-width="4" fill="none"/></svg>
<div class="abs medal"><div class="medal-inner" role="img" aria-label="Customer portrait silhouette"></div></div>
<p class="abs quote">Delicious beans and fast delivery. I'll be back!</p>
<p class="abs quote-body">Lorem ipsum dolor sit amet, consectetuer adipiscing elitsed diam nonummy nibh euismod tincidunt ut laoreet dolore magna aliquam erat volutpat. Ut wisi enim ad minim veniam, quis nostrud exerci tation ullamcorper suscipit lobortis nisl ut aliquip ex ea commodiwsi enim ad minim veniam, quis nostrud exerci tation ullamcorper suscipit lobortis nisl ut consequat.</p>
<p class="abs quote-name">Mr. Minim Veniam</p>
<div class="abs dots"><span></span><span></span><span></span><span></span></div>

<div class="abs footer"></div>
<div class="abs foot-head" style="left:85px;top:2592px">ABOUT STORE</div>
<p class="abs foot-text" style="left:85px;top:2626px;width:290px">Lorem ipsum dolomeconsectetuer adipiscing elit, sed diam nonummibh euismod tincidunt ut laoreet dolore magna aliquam erat. Lorem ipsum dolomeconsectetuer adipiscing elit, sed diam nonummibh euismod.</p>
<div class="abs foot-head" style="left:435px;top:2592px">NAVIGATION</div>
<div class="abs foot-nav" style="left:435px;top:2628px">
  <span>Home</span><span>Delivery</span><span>About Us</span><span>Faqs</span><span>Shop</span><span>Contact Us</span><span>Blog</span><span>My Account</span>
</div>
<div class="abs foot-head" style="left:672px;top:2592px">LATEST POST</div>
<div class="abs post-thumb" role="img" aria-label="Blog post thumbnail of a cat on a pink blanket"></div>
<p class="abs foot-text" style="left:825px;top:2628px;width:290px;font-weight:700;color:#fff">Lorem ipsum dolomecons tetuer adipiscing elit, sed diam nonummibh.</p>
<p class="abs foot-text" style="left:825px;top:2670px;width:290px">Dorem ipsum dolomecons tetuer adipiscing elit, sed diam nonummibh, dolomecons tetuer adipis.</p>
<p class="abs post-date" style="left:825px;top:2730px">13 Sep, 2017</p>

<div class="abs subscribe"></div>
<div class="abs sub-title">SUBSCRIBE TO US!</div>
<div class="abs sub-text">Subscribe to our monthly Newsletter</div>
<div class="abs sub-input">Enter your email here
  <svg style="position:absolute;right:18px;top:15px" width="14" height="10" viewBox="0 0 14 10" aria-hidden="true"><rect x="0.5" y="0.5" width="13" height="9" fill="#fff"/><path d="M0.5 0.5 7 6 13.5 0.5" stroke="#5bb9e4" fill="none"/></svg>
</div>
<div class="abs social" style="left:968px" role="img" aria-label="Social network link"></div>
<div class="abs social" style="left:1032px" role="img" aria-label="Social network link"></div>
<div class="abs social" style="left:1093px" role="img" aria-label="Social network link"></div>
<div class="abs copy-rule"></div>
<div class="abs copyright">Copyrights © All Rights Reserved 2017</div>

</body>
</html>
```